Business Card Design

We do Metal Roofing, fascia and gutter and edge protection [safety rail].

Industry/Entity Type

Business

Contact Information for Business Card

Tallowind Roof Plumbing. Metal Roofing, Fascia and Gutter, Edge Protection
Corey 0458316072
Liam 0419563284
kv7lem4@tullanet.com
Lic: 618390K
ABN:57214603915

```html
<!DOCTYPE html>
<html lang="en">
<head>
<meta charset="utf-8">
<title>Tallowind Roof Plumbing – Business Card</title>
<link rel="stylesheet" href="https://fonts.googleapis.com/css2?family=Figtree:wght@400;700;800&display=swap">
<style>
  :root {
    --brand-blue: #0d4fa3;
    --text-grey: #8d949c;
    --bar-grey: #9ea5ad;
    --card-white: #ffffff;
    --backdrop: #e9e7e3;
  }
  * { margin: 0; padding: 0; box-sizing: border-box; }
  html, body {
    width: 1200px;
    height: 1000px;
    overflow: hidden;
    background: var(--backdrop);
    font-family: "Figtree", Arial, sans-serif;
  }
  .canvas {
    position: relative;
    width: 1200px;
    height: 1000px;
  }
  .business-card {
    position: absolute;
    left: 266.5px;
    top: 301.5px;
    width: 667px;
    height: 397px;
    background: var(--card-white);
    box-shadow: 0 6px 22px rgba(0,0,0,0.18);
    transform: scale(1.35);
    transform-origin: center;
  }
  .contacts {
    position: absolute;
    left: 39px;
    top: 76px;
  }
  .person-name {
    color: var(--brand-blue);
    font-weight: 700;
    font-size: 21px;
    line-height: 24px;
  }
  .phone-line {
    display: flex;
    align-items: center;
    gap: 6px;
    color: var(--text-grey);
    font-size: 17px;
    line-height: 22px;
    margin-bottom: 24px;
  }
  .phone-line svg { width: 12px; height: 12px; fill: var(--text-grey); }
  .registration {
    font-size: 17px;
    line-height: 30px;
    color: var(--text-grey);
    margin-top: -2px;
  }
  .registration .label { color: var(--brand-blue); font-weight: 700; }
  .email-line {
    display: flex;
    align-items: center;
    gap: 8px;
    margin-top: 8px;
    color: var(--text-grey);
    font-size: 17px;
  }
  .email-line svg { width: 15px; height: 11px; }
  .brand-name {
    position: absolute;
    left: 342px;
    top: 58px;
    width: 286px;
    color: var(--brand-blue);
    font-weight: 800;
    text-align: center;
    line-height: 1;
  }
  .brand-name .brand-main { display: block; font-size: 50px; letter-spacing: 1px; }
  .brand-name .brand-sub { display: block; font-size: 30px; margin-top: 34px; }
  .services {
    position: absolute;
    left: 349px;
    top: 243px;
    list-style: none;
  }
  .services li {
    display: flex;
    align-items: center;
    gap: 8px;
    color: var(--text-grey);
    font-size: 17px;
    line-height: 24px;
  }
  .services svg { width: 16px; height: 16px; }
  .footer-bar {
    position: absolute;
    bottom: 0;
    height: 25px;
  }
  .footer-bar.grey { left: 0; width: 335px; background: var(--bar-grey); }
  .footer-bar.blue { left: 342px; right: 0; background: var(--brand-blue); }
</style>
</head>
<body>
<div class="canvas">
  <div class="business-card">
    <div class="contacts">
      <div class="person-name">Corey</div>
      <div class="phone-line">
        <svg viewBox="0 0 24 24" aria-hidden="true"><path d="M6.6 10.8a15.1 15.1 0 0 0 6.6 6.6l2.2-2.2a1 1 0 0 1 1-.25 11.4 11.4 0 0 0 3.6.57 1 1 0 0 1 1 1V20a1 1 0 0 1-1 1A17 17 0 0 1 3 4a1 1 0 0 1 1-1h3.5a1 1 0 0 1 1 1c0 1.25.2 2.45.57 3.57a1 1 0 0 1-.25 1z"/></svg>
        <span>0458316072</span>
      </div>
      <div class="person-name">Liam</div>
      <div class="phone-line">
        <svg viewBox="0 0 24 24" aria-hidden="true"><path d="M6.6 10.8a15.1 15.1 0 0 0 6.6 6.6l2.2-2.2a1 1 0 0 1 1-.25 11.4 11.4 0 0 0 3.6.57 1 1 0 0 1 1 1V20a1 1 0 0 1-1 1A17 17 0 0 1 3 4a1 1 0 0 1 1-1h3.5a1 1 0 0 1 1 1c0 1.25.2 2.45.57 3.57a1 1 0 0 1-.25 1z"/></svg>
        <span>0419563284</span>
      </div>
      <div class="registration"><span class="label">Lic #</span> 618390K</div>
      <div class="registration"><span class="label">ABN #</span> 57214603915</div>
      <div class="email-line">
        <svg viewBox="0 0 15 11" aria-hidden="true"><rect width="15" height="11" fill="#0d4fa3"/><path d="M0 0l7.5 6L15 0" fill="none" stroke="#fff" stroke-width="1.3"/></svg>
        <span>kv7lem4@tullanet.com</span>
      </div>
    </div>

    <div class="brand-name">
      <span class="brand-main">TALLOWIND</span>
      <span class="brand-sub">ROOF PLUMBING</span>
    </div>

    <ul class="services">
      <li><svg viewBox="0 0 16 16" aria-hidden="true"><rect x="1" y="2" width="12" height="12" fill="none" stroke="#0d4fa3" stroke-width="1.8"/><path d="M4 7.5l3 3 7-8" fill="none" stroke="#0d4fa3" stroke-width="2"/></svg>Metal Roofing</li>
      <li><svg viewBox="0 0 16 16" aria-hidden="true"><rect x="1" y="2" width="12" height="12" fill="none" stroke="#0d4fa3" stroke-width="1.8"/><path d="M4 7.5l3 3 7-8" fill="none" stroke="#0d4fa3" stroke-width="2"/></svg>Fascia</li>
      <li><svg viewBox="0 0 16 16" aria-hidden="true"><rect x="1" y="2" width="12" height="12" fill="none" stroke="#0d4fa3" stroke-width="1.8"/><path d="M4 7.5l3 3 7-8" fill="none" stroke="#0d4fa3" stroke-width="2"/></svg>Gutter</li>
      <li><svg viewBox="0 0 16 16" aria-hidden="true"><rect x="1" y="2" width="12" height="12" fill="none" stroke="#0d4fa3" stroke-width="1.8"/><path d="M4 7.5l3 3 7-8" fill="none" stroke="#0d4fa3" stroke-width="2"/></svg>Edge Protection</li>
    </ul>

    <div class="footer-bar grey"></div>
    <div class="footer-bar blue"></div>
  </div>
</div>
</body>
</html>
```